Website for New Phone Company

Our company "Lagoonfield Telecom" requires a new web-site.

We enable Pacific Islanders (Fijians, Samoans, Tongans) to speak to their friends and family back home for a fraction of the cost of other phone companies whilst maintaining a quality. Our target audience is price sensitive but is demanding with quality, we would like them to gather a feel that they are dealing with a safe company that is orientated towards the Pacific Island community, has low pricing and yet doesn't compromise on quality.

We are going to be marketing via online channels and so a Google friendly web-site is important. We essentially need three pages designed which we will use with our content.

Page 1 - Homepage Lagoonfield Telecom - Our prime brand is Lagoonfield Telecom and we would like to promote this brand on our web-site.

However, we have three plans under this brand called Miroka, Selavi and Penuko. We would like the main page to have three unique service offerings for Penuko, Selavi and Miroka. Something along the lines of being able to choose a plan down on the page. I would like to give examples here of companies in our industry that are extremely successful in this trade i.e. www.ringvelo.co.nz, www.9speakly.co.nz, www.quorlix.com

The objective of this design is to present the customer with three unique offerings targeted to Samoa (Penuko), Selavi (Tonga) and Miroka (Fiji).

Page 2 - Content/Template Page for Lagoonfield Telecom - We require a page where we can place content like About Us, Contact Us etc.

Page 3 - We require a single design that will fit all three brands as per the brand images attached for Miroka, Penuko and Selavi. This will almost be used as a landing page to brand the plan exclusively under our company. All three plans / service offerings are being marketed under "Lagoonfield Telecom" which makes it important to use both the service offering logo as well as the company logo. This page needs to act more as a promotional page where it promotes our service offering. e.g. Call Samoa from only 50c a minute type of thing.

The objective of the design of the landing / service offering page is to entice the customer to act upon the offer by joining our organisation.

We will be available throughout the process to guide you better.
Updates

Reason: We haven't received suitable designs to choose from. We would like to see quality work not quantity.

Industry/Entity Type

It Company

```html
<!DOCTYPE html>
<html lang="en">
<head>
<meta charset="utf-8">
<title>Lagoonfield Telecom</title>
<link href="https://fonts.googleapis.com/css2?family=Arimo:wght@400;700&family=Montserrat:wght@400;700&family=Tinos:wght@400;700&display=swap" rel="stylesheet">
<style>
:root{
  --ink:#222;
  --grey:#777;
  --rule:#c9c9c9;
  --red:#d7261e;
  --blue:#0a5ea6;
  --brown:#9b3f26;
  --lime:#8fd53a;
  --sand:#ebe4c0;
  --link:#0b6fb3;
  --mint:#a8f0b0;
  --cream:#f8eeb4;
}
*{box-sizing:border-box;margin:0;padding:0}
html,body{width:1200px;height:1030px;overflow:hidden;background:#fff}
body{position:relative;font-family:Arimo,Arial,sans-serif;color:var(--ink)}
.site-header{position:absolute;left:0;top:0;width:1200px;height:111px;border-bottom:3px solid var(--rule)}
.brand{position:absolute;left:44px;top:16px;display:flex;align-items:center;gap:20px}
.brand-dot{width:84px;height:84px;border-radius:50%;background:var(--red)}
.brand-name{font-family:Montserrat,Arial,sans-serif;font-weight:700;font-size:36px;line-height:40px;color:var(--grey);width:240px}
.social{position:absolute;top:20px;right:34px;display:flex;align-items:center;gap:34px;font-size:13px;color:#333}
.social span{display:flex;align-items:center;gap:6px}
.sq{display:inline-block;width:20px;height:20px}
.share{display:flex}
.share .sq{background:#e0e0e0;border:1px solid #c33}
.share .count{border:1px solid #ccc;font-size:11px;padding:2px 6px;color:#c33}
.nav{position:absolute;top:76px;right:34px;display:flex;gap:29px;font-family:Montserrat,Arial,sans-serif;font-size:13.5px;font-weight:700;letter-spacing:.3px;color:#222;list-style:none}
.hero{position:absolute;left:0;top:114px;width:1200px;height:407px;background:linear-gradient(180deg,#d9dfd6 0%,#cfd6c0 25%,#7fa047 42%,#4f7b25 70%,#3d5d1c 100%)}
.hero-scene{position:absolute;inset:0}
.hero-pitch{position:absolute;left:724px;top:68px;width:413px;height:253px;background:rgba(40,48,35,.7);padding:24px 32px;font-family:Montserrat,Arial,sans-serif;font-weight:700;font-size:20px;line-height:40px;color:#fff}
.hero-pitch .mint{color:var(--mint);font-size:30px}
.hero-pitch .cream{color:var(--cream);font-size:31px}
.plans{position:absolute;left:0;top:521px;width:898px;height:122px;display:flex;gap:3px;background:var(--rule);border:2px solid var(--rule);border-left:0}
.plan{flex:1;min-width:0;display:flex;align-items:center;justify-content:space-between;padding:0 10px 0 12px;color:#fff;font-family:Montserrat,Arial,sans-serif;font-weight:700;white-space:nowrap;overflow:hidden}
.plan-blue{background:var(--blue)}
.plan-red{background:var(--red)}
.plan-brown{background:var(--brown)}
.plan-id{display:flex;flex-direction:column;align-items:center;gap:6px;margin-top:8px}
.plan-mark{width:40px;height:40px;border-radius:50%;background:#fff}
.plan-name{font-size:21px;font-weight:400;letter-spacing:.5px}
.plan-price{font-size:52px;letter-spacing:-2px;line-height:1}
.plan-price small{font-size:19px;letter-spacing:0}
.plan-red .plan-price,.plan-red .plan-name{color:var(--lime)}
.welcome{position:absolute;left:30px;top:664px;width:840px}
.welcome h1{font-family:Tinos,serif;font-weight:400;font-size:22px;color:#333;display:flex;align-items:center;gap:8px}
.welcome h1 b{color:var(--red);font-weight:400}
.welcome h2{font-size:14px;font-weight:700;color:#0f2a3a;margin:18px 0 18px}
.welcome p{font-size:11.5px;line-height:16px;color:#333}
.welcome a{color:var(--link);text-decoration:underline}
.intro{display:flex;gap:16px;margin-bottom:18px}
.intro-photo{width:142px;height:101px;border-radius:6px;flex:none;background:linear-gradient(135deg,#8aa0b8,#5c6b7c 60%,#a3a6a0)}
.btn{position:absolute;right:2px;top:260px;width:95px;height:26px;border-radius:5px;background:linear-gradient(#f05a4a,#c8170f);color:#fff;font-size:12px;font-weight:700;text-align:center;line-height:26px}
.spotlight{position:absolute;left:898px;top:521px;width:302px;height:453px;background:var(--sand);border:3px solid var(--rule);padding:16px 16px 0 16px}
.spotlight h3{font-family:Tinos,serif;font-size:24px;font-weight:700;color:#1c1c1c;margin-bottom:14px}
.news{margin-bottom:28px}
.news-head{display:flex;gap:10px;align-items:flex-end}
.cal{width:38px;text-align:center;font-size:11px;font-weight:700}
.cal div{background:var(--red);color:#fff;font-size:16px;border-radius:4px;padding:4px 0}
.news-date{font-size:12px;color:var(--red);text-decoration:underline;margin-bottom:2px}
.news-title{font-size:12px;font-weight:700;color:#000}
.news p{font-size:12px;line-height:18px;color:#333;margin:8px 2px 10px}
.more{font-size:12px;color:var(--link);text-decoration:underline;display:flex;align-items:center;gap:6px}
.more i{width:13px;height:13px;border-radius:50%;border:1px solid #aaa;background:#fff}
.site-footer{position:absolute;left:0;top:971px;width:1200px;height:59px;border-top:3px solid var(--rule);font-size:11px;color:#222;padding:24px 30px}
</style>
</head>
<body>
<header class="site-header">
  <div class="brand"><span class="brand-dot"></span><span class="brand-name">Lagoonfield Telecom</span></div>
  <div class="social">
    <span class="share"><i class="sq"></i><span class="count">1</span></span>
    <span><i class="sq" style="background:#3b5998"></i>Join us</span>
    <span><i class="sq" style="background:#2aa3d6"></i>Follow us</span>
  </div>
  <ul class="nav"><li>HOME</li><li>PHONECARDS</li><li>RECHARGE</li><li>PRODUCTS</li><li>ABOUT US</li><li>CONTACT</li></ul>
</header>

<section class="hero">
  <div class="hero-scene" role="img" aria-label="Businessman relaxing at a desk with a laptop in an open green field"></div>
  <div class="hero-pitch">Doesn’t matter <span class="mint">wherever</span><br>you are, just get <span class="cream">connected</span><br>using our <span class="mint">economical</span><br>services without compromising<br>on <span class="cream">quality</span> of voice.</div>
</section>

<section class="plans">
  <div class="plan plan-blue"><span class="plan-id"><span class="plan-mark"></span><span class="plan-name">Penuko</span></span><span class="plan-price">$7<small>.79/month</small></span></div>
  <div class="plan plan-red"><span class="plan-id"><span class="plan-mark"></span><span class="plan-name">Selavi</span></span><span class="plan-price">$8<small>.99/month</small></span></div>
  <div class="plan plan-brown"><span class="plan-id"><span class="plan-mark"></span><span class="plan-name">Miroka</span></span><span class="plan-price">$9<small>.99/month</small></span></div>
</section>

<main class="welcome">
  <h1><svg width="24" height="22" viewBox="0 0 24 22"><path d="M0 0 L12 22 L24 0 L12 10 Z" fill="#0a5ea6"/></svg><b>WELCOME</b> to Lagoonfield Telecom</h1>
  <h2>Voluptatem accusantium doloremque laudantium,totamest rem aperiam, eaquesel</h2>
  <div class="intro">
    <div class="intro-photo" role="img" aria-label="Woman reading a booklet in front of a city building"></div>
    <p>Aut perspiciatis unde omnis istnatus sit voluptatem accusantiumedel doloreque laudantium, totam rem aperiam, eaque ipssi architectori beatae vitae dicta sunt explicaboNemo enim ipsam voluptatem quiac voluptas sit <a>aspernatur aut odit aut fugit, sed quia consequunturumes</a> magni dolores eos qui rationede voluptatem sequi nesciunt. Neque porro quisquam est, qui dolorem ipsum quia dolor sit ame consectetur, adipisci velit, sedol quia non numquam eius modi. nem ullam corporis suscipit laboriosam, nisi ut aliquid ex ea commodi consequatur? Quis autem vel eum iure reprehenderit qui in ea voluptate velit esse quam nihil molestiae consequatur, vel illum qui dolorem eum fugiat quo voluptas nulla pariatur?</p>
  </div>
  <p>agni dolores eos qui rationede voluptatem sequi nesciunt. Neque porro quisquam est, qui dolorem ipsum quia dolor sit ame consectetur, adipisci velit, sedol quia non numquam eius modi. nem ullam corporis suscipit laboriosam, nisi ut aliquid ex ea commodi consequatur? Quis autem vel eum iure reprehenderit qui in ea voluptate velit esse quam nihil molestiae consequatur, vel illum qui dolorem eum fugiat quo voluptas nulla pariatur.</p>
  <span class="btn">Read More</span>
</main>

<aside class="spotlight">
  <h3>In The Spotlight</h3>
  <div class="news">
    <div class="news-head"><div class="cal">Sep<div>30</div></div><div><div class="news-date">30.09.2013</div><div class="news-title">Doloremquedesaudantimdic totam</div></div></div>
    <p>Werspiciatis unde omnis istnatus situm desasec voluptatem asdoloremquedesaudantimdic totam remi aperi eaque ipssivitaeco dicta sunt</p>
    <span class="more"><i></i>Read More</span>
  </div>
  <div class="news">
    <div class="news-head"><div class="cal">Sep<div>20</div></div><div><div class="news-date">20.09.2013</div><div class="news-title">Doloremquedesaudantimdic totam</div></div></div>
    <p>Werspiciatis unde omnis istnatus situm desasec voluptatem asdoloremquedesaudantimdic totam remi aperi eaque ipssivitaeco dicta sunt exibition explicabooenimedelipsamvoluptateol quia</p>
    <span class="more"><i></i>Read More</span>
  </div>
</aside>

<footer class="site-footer">Copyright 2014 Lagoonfield Telecom, All rights reserved.</footer>
</body>
</html>
```